Realtor Website Design

We are working with QOV•ZAR. They are a financial advising company that needs a new website design.

Some sites to use for inspiration:

https://www.dapomirle.com
https://www.vosbaquirealty.com

Thank you for taking the time to consider designing a website for us. We are web developers based in Stockton and Los Angeles, CA, USA. Most of our projects go through the same process. Understanding this process may help you win a project with us. We custom-code all of our websites in-house. We don’t have any requirements as to what tools you use for your design, but we prefer Figma files. For any design that we label as four-stars, we send it to the client for review. The client picks the final design they want us to use. Once we complete this process, we will continue to show additional clients all the four-star sites and purchase them later. Your designs will have multiple chances to sell. For better chances of success, we ask that you follow these guidelines.

IMAGES:
If you use any images or icons in the design, we ask that you have a link to the asset so we can purchase the image/icon. Most of the designs we submit do not have the customer’s images on them unless they have some great images. Be creative; show us the feeling you are trying to portray with your image choices. Use any royalty-free site you choose. We subscribe to Vantrel and mainly use their images, but we can purchase images outside of Vantrel.

PLEASE NOTE: we will not submit designs to clients with watermarks on the images.

FONTS:
We ask that you identify the fonts used in the design. This can be done in a message if you want. We typically use Zumbix Fonts and Vantrel Fonts.

CONTENT:
We're always open to different content and ideas. We often submit designs with stock images so the client can see our vision. We typically take pictures after the website launch to use their images with our vision. Lorem Ipsum is fine for paragraphs, but we ask that you write the headers in correct English. We want to be able to show the vision and identify the sections of the website.

INSPIRATION:
We typically add a couple of links in the brief of websites we like to help you get started in your design.

REVISIONS:
We do not often ask for revisions of the designs unless we see something in the design that may not appeal to the client. If there are slight changes that we want to make, we do that in the development process.

FEEDBACK:
We rarely give feedback on designs during the design process. We are working on many website projects and do not have the time to provide feedback. We usually respond if your request is well thought out and asks specific questions, but a note asking “feedback, please” usually goes unanswered.

```html
<!DOCTYPE html>
<html lang="en">
<head>
<meta charset="utf-8">
<title>Homes by Marlowe</title>
<link href="https://fonts.googleapis.com/css2?family=EB+Garamond:wght@400;500;600&family=Lato:wght@400;700&display=swap" rel="stylesheet">
<style>
:root{
  --teal:#3a958e;
  --teal-dark:#2f7d77;
  --teal-deep:#1f5f5a;
  --mint:#e3f1ee;
  --mint-2:#cfe6e1;
  --ink:#1d2326;
  --muted:#5b6467;
  --white:#ffffff;
  --paper:#f4f5f5;
  --star:#f2a531;
}
*{box-sizing:border-box;margin:0;padding:0}
html,body{width:1200px;height:4096px;overflow:hidden}
body{font-family:"EB Garamond",Georgia,serif;color:var(--ink);background:var(--white);position:relative}
.section{position:absolute;left:0;width:1200px}
.btn{display:inline-block;background:var(--teal);color:var(--white);font-family:"Lato",Arial,sans-serif;font-weight:700;font-size:15px;padding:14px 28px;border-radius:26px}
.btn-wrap{position:relative;display:inline-block}
.btn-dot{position:absolute;right:-22px;bottom:-6px;width:16px;height:16px;border-radius:4px;background:var(--teal-deep)}
h2{font-weight:500;font-size:44px;line-height:1.15}
p.body{font-size:15px;line-height:1.55;color:var(--muted)}

/* hero */
.hero{top:0;height:580px;background:linear-gradient(100deg,#2a2d2c 0%,#4b4a45 35%,#6d665b 55%,#3c3d38 80%,#2b3130 100%)}
.hero-shade{position:absolute;inset:0;background:linear-gradient(90deg,rgba(0,0,0,.55),rgba(0,0,0,.1) 60%,rgba(0,0,0,.25))}
.nav{position:absolute;top:28px;left:110px;right:110px;display:flex;align-items:center;justify-content:space-between}
.brand{display:flex;align-items:center;gap:12px;color:var(--white);font-size:30px;font-weight:500}
.brand-mark{width:22px;height:22px;border-radius:50%;background:var(--teal)}
.nav-links{display:flex;gap:12px;font-size:17px;color:var(--white)}
.nav-links span{padding:8px 14px;border-radius:6px}
.nav-links .active{background:var(--teal)}
.hero-brand{position:absolute;left:110px;top:290px;display:flex;align-items:center;gap:14px;color:var(--mint-2);font-size:40px;font-weight:500}
.hero-brand .brand-mark{width:34px;height:34px}
.hero h1{position:absolute;left:110px;top:390px;color:var(--white);font-weight:500;font-size:54px}
.hero .btn-wrap{position:absolute;left:110px;top:470px}

/* intro */
.intro{top:580px;height:620px;background:linear-gradient(180deg,var(--white) 0%,var(--mint) 60%,var(--mint-2) 100%)}
.intro h2{position:absolute;left:110px;top:95px;width:540px}
.intro-brand{position:absolute;left:110px;top:240px;display:flex;align-items:center;gap:18px;color:var(--teal);font-size:56px;font-weight:500}
.intro-brand .brand-mark{width:44px;height:44px;border-radius:50%;background:var(--teal)}
.intro-copy{position:absolute;left:690px;top:110px;width:400px}
.intro-copy p{margin-bottom:20px}
.intro-copy .btn-wrap{margin-top:6px}

/* split rows */
.advisor{top:1200px;height:640px;background:var(--white)}
.advisor .text{position:absolute;left:110px;top:120px;width:430px}
.advisor .photo{position:absolute;left:600px;top:90px;width:600px;height:480px;background:linear-gradient(120deg,#cfd8d8,#9fb0b2 50%,#6f5a4a 75%,#d6dcdb)}
.partner{top:1840px;height:610px;background:linear-gradient(180deg,#f3f3f3,#fafafa)}
.partner .photo{position:absolute;left:0;top:0;width:580px;height:520px;background:linear-gradient(120deg,#eeeeec,#d9d6d0 50%,#a68d75 70%,#e8e6e2)}
.partner .text{position:absolute;left:660px;top:130px;width:440px}
.text h2{margin-bottom:22px}
.text p{margin-bottom:18px}
.text .btn-wrap{margin-top:8px}

/* properties */
.properties{top:2450px;height:580px;background:linear-gradient(180deg,#e9f4f2,#f7fbfa)}
.center-title{position:absolute;left:0;width:1200px;text-align:center}
.properties .center-title{top:80px}
.cards{position:absolute;left:28px;top:162px;display:flex;gap:22px}
.card{width:365px;background:var(--white);box-shadow:0 2px 10px rgba(0,0,0,.08)}
.card .img{height:230px}
.card .cap{padding:16px 0 20px;text-align:center;border-top:1px solid #e5e5e5}
.card .cap h3{font-family:"Lato",Arial,sans-serif;font-weight:700;font-size:17px;margin-bottom:8px}
.card .cap div{font-family:"Lato",Arial,sans-serif;font-size:13px;color:var(--muted)}

/* reviews */
.reviews{top:3030px;height:610px;background:var(--white)}
.reviews .center-title{top:55px}
.review{position:absolute;background:var(--white);border:1px solid #e6e6e6;padding:24px 28px;font-size:15px;line-height:1.45;color:var(--muted)}
.review .stars{color:var(--star);font-size:15px;letter-spacing:2px;margin-bottom:12px}
.review .who{font-family:"Lato",Arial,sans-serif;font-weight:700;font-size:14px;color:var(--ink);margin-top:18px}
.review .role{font-family:"Lato",Arial,sans-serif;font-size:12px;color:#9aa1a3;margin-top:4px}
.review.featured{box-shadow:0 6px 24px rgba(0,0,0,.14);border:none}
.review.featured .who,.review.featured .role{color:var(--teal)}

/* footer */
.footer{top:3640px;height:456px;background:var(--teal);color:var(--white);font-family:"Lato",Arial,sans-serif}
.footer h4{font-size:14px;font-weight:700;margin-bottom:24px}
.col-links{position:absolute;left:110px;top:90px}
.col-links li{list-style:none;font-size:12px;margin-bottom:14px;display:flex;align-items:center;gap:10px}
.col-links li::before{content:"";width:5px;height:5px;border-radius:50%;background:var(--white)}
.col-contact{position:absolute;left:320px;top:90px}
.contact-row{display:flex;align-items:center;gap:14px;font-size:12px;margin-bottom:20px;line-height:1.4}
.icon-circle{width:34px;height:34px;border-radius:50%;border:1.5px solid var(--white);display:flex;align-items:center;justify-content:center}
.col-form{position:absolute;left:636px;top:90px;width:452px}
.field{background:var(--white);color:#8a9395;font-size:11px;padding:7px 10px;border-radius:2px}
.row2{display:flex;gap:12px;margin-bottom:12px}
.row2 .field{flex:1}
.field.full{margin-bottom:12px}
.field.msg{height:86px}
.submit{float:right;margin-top:12px;background:var(--white);color:var(--teal-dark);font-weight:700;font-size:11px;padding:7px 16px;border-radius:14px}
.socials{position:absolute;right:112px;top:386px;display:flex;gap:8px}
.socials span{width:26px;height:26px;border-radius:50%;border:1.5px solid var(--white)}
.copyright{position:absolute;left:0;top:424px;width:1200px;height:32px;background:var(--teal-dark);padding:10px 110px;font-size:11px}
</style>
</head>
<body>

<header class="section hero">
  <div class="hero-shade" role="img" aria-label="Photo of a modern home patio with stone fireplace and lounge chairs at dusk"></div>
  <nav class="nav">
    <div class="brand"><span class="brand-mark"></span>Marlowe</div>
    <div class="nav-links">
      <span class="active">Home</span><span>Our Team</span><span>Reviews</span><span>Buy a Home</span><span>Sell a Home</span><span>Contact</span>
    </div>
  </nav>
  <div class="hero-brand"><span class="brand-mark"></span>Homes by Marlowe</div>
  <h1>Find the Home That Fits Your Life</h1>
  <div class="btn-wrap"><span class="btn">Work With Marlowe</span></div>
</header>

<section class="section intro">
  <h2>Representing Buyers and Sellers Homes by Marlowe</h2>
  <div class="intro-brand"><span class="brand-mark"></span>Homes by Marlowe</div>
  <div class="intro-copy">
    <p class="body">Whether you're buying your first home or selling a cherished property, Marlowe brings experience, strategy, and heart to every step. She listens closely, provides honest guidance, and ensures you feel confident — from your first showing to the final signature. With deep local expertise and modern marketing tools, Homes by Marlowe delivers results that move you forward.</p>
    <p class="body">Buying a home can be exciting — and overwhelming. Marlowe works closely with buyers to identify the right neighborhoods, evaluate market opportunities, and negotiate confidently.</p>
    <div class="btn-wrap"><span class="btn">Read More</span><span class="btn-dot"></span></div>
  </div>
</section>

<section class="section advisor">
  <div class="text">
    <h2>Trusted Advisor. Results-Driven. Relationship first.</h2>
    <p class="body">Lorem ipsum dolor sit amet, consectetur adipiscing elit, sed do eiusmod tempor incididunt ut labore et dolore magna aliqua. Ut enim ad minim veniam, quis nostrud exercitation ullamco laboris nisi ut aliquip ex ea commodo consequat.</p>
    <p class="body">Duis aute irure dolor in reprehenderit in voluptate velit esse cillum dolore eu fugiat nulla pariatur et ex laborum.</p>
    <div class="btn-wrap"><span class="btn">Read More</span><span class="btn-dot"></span></div>
  </div>
  <div class="photo" role="img" aria-label="Photo of a realtor in a brown jacket holding a folder in a bright office"></div>
</section>

<section class="section partner">
  <div class="photo" role="img" aria-label="Photo of a smiling advisor with glasses working on a laptop"></div>
  <div class="text">
    <h2>Partnering with Buyers and Sellers at Every Price Point</h2>
    <p class="body">Lorem ipsum dolor sit amet, consectetur adipiscing elit, sed do eiusmod tempor incididunt ut labore et dolore magna aliqua. Ut enim ad minim veniam, quis nostrud exercitation ullamco laboris.</p>
    <p class="body">Duis aute irure dolor in reprehenderit in voluptate velit esse cillum dolore eu fugiat nulla pariatur.</p>
    <div class="btn-wrap"><span class="btn">Read More</span><span class="btn-dot"></span></div>
  </div>
</section>

<section class="section properties">
  <h2 class="center-title">Featured Properties</h2>
  <div class="cards">
    <article class="card">
      <div class="img" role="img" aria-label="Photo of a bright living room with beige sofas" style="background:linear-gradient(135deg,#d8cfc2,#a8978a 55%,#6e625a)"></div>
      <div class="cap"><h3>Excepteur sint | Leura</h3><div>5 Beds | 7 Baths | 16 Guests</div></div>
    </article>
    <article class="card">
      <div class="img" role="img" aria-label="Photo of an open-plan living and dining room with wood floors" style="background:linear-gradient(135deg,#e9e4dc,#b9a58e 55%,#7c6a57)"></div>
      <div class="cap"><h3>Duis aute irure dolor | Woodford</h3><div>3 Beds | 7 Baths | 10 Guests</div></div>
    </article>
    <article class="card">
      <div class="img" role="img" aria-label="Photo of a white kitchen with a large island" style="background:linear-gradient(135deg,#f1f0ec,#cfc9c0 55%,#9a8f84)"></div>
      <div class="cap"><h3>Lorem ipsum dolor</h3><div>16 Beds | 12 Baths | 26 Guests</div></div>
    </article>
  </div>
</section>

<section class="section reviews">
  <h2 class="center-title">What Our Customer Says</h2>
  <div class="review" style="left:110px;top:160px;width:322px;height:260px">
    <div class="stars">★★★★★</div>
    We were nervous first-time buyers, but Marlowe guided us through every step with patience and confidence. She understood what we wanted, found options that fit our budget, and negotiated an amazing deal.
    <div class="who">Renata Colby</div><div class="role">Marlowe made buying our first home feel easy.</div>
  </div>
  <div class="review featured" style="left:452px;top:190px;width:314px;height:290px">
    <div class="stars">★★★★★</div>
    Marlowe handled everything — from staging and photos to pricing and marketing — with total professionalism. Her communication was excellent, and she made the process completely stress-free. Thank You!
    <div class="who">Mirela Stanton</div><div class="role">Our home sold in less than a week!</div>
  </div>
  <div class="review" style="left:786px;top:160px;width:304px;height:260px">
    <div class="stars">★★★★★</div>
    Marlowe wasn't just our agent — she was our advocate. She took the time to learn our lifestyle, stayed on top of every detail, and made sure we felt comfortable at every stage.
    <div class="who">Owen Harkley</div><div class="role">She truly cared about finding the right home for us.</div>
  </div>
</section>

<footer class="section footer">
  <div class="col-links">
    <h4>Useful Links</h4>
    <ul><li>Home</li><li>About</li><li>Properties</li><li>Testimonials</li><li>Buy and Sell</li><li>Contact</li></ul>
  </div>
  <div class="col-contact">
    <h4>Contact Information</h4>
    <div class="contact-row"><span class="icon-circle"><svg width="14" height="16" viewBox="0 0 14 16"><path d="M7 1a5 5 0 0 0-5 5c0 4 5 9 5 9s5-5 5-9a5 5 0 0 0-5-5z" fill="none" stroke="#fff" stroke-width="1.5"/><circle cx="7" cy="6" r="1.8" fill="#fff"/></svg></span><span>Homes by Marlowe<br>United States</span></div>
    <div class="contact-row"><span class="icon-circle"><svg width="14" height="14" viewBox="0 0 14 14"><path d="M3 1l2 3-1.5 1.5c.8 1.8 2.2 3.2 4 4L9 8l3 2-1 3C6 13 1 8 1 3z" fill="none" stroke="#fff" stroke-width="1.4" stroke-linejoin="round"/></svg></span><span>Phone: +1 000 000 0000</span></div>
    <div class="contact-row"><span class="icon-circle"><svg width="16" height="12" viewBox="0 0 16 12"><rect x="1" y="1" width="14" height="10" fill="none" stroke="#fff" stroke-width="1.4"/><path d="M1 1l7 6 7-6" fill="none" stroke="#fff" stroke-width="1.4"/></svg></span><span>Email: info@homesbymarlowe.com</span></div>
  </div>
  <div class="col-form">
    <h4>Get In Touch:</h4>
    <div class="row2"><div class="field">Name</div><div class="field">Phone</div></div>
    <div class="field full">Email</div>
    <div class="field msg">Message</div>
    <span class="submit">SUBMIT</span>
  </div>
  <div class="socials"><span></span><span></span><span></span><span></span></div>
  <div class="copyright">Copyright © 2023 Homes by Marlowe. All Rights Reserved. | Privacy policy</div>
</footer>

</body>
</html>
```